prestige web design for KELVA Finance

Hi Guys,

Looking to team up with a creative designer for another of our websites for KELVA finance.
if looking for our similar website www.brimlendco.com.au is one of our other companies. ideally working in our logo being black and white.

Please see attachments for our logo and a description
HOME
VEHICLE
EQUIPMENT
WHO WE ARE
CONTACT US

open to ideas on layout .

touch base if you have any questions.

Target Market(s)

Prestige cars and equipment -trucks earthmoving

Industry/Entity Type

finance

Coding

Coded - Design and coding required

Number of Pages Required

5+ page

Font styles to use
Sans Serif

Colors

Designer to choose colors to be used in the design.

```html
<!DOCTYPE html>
<html lang="en">
<head>
<meta charset="utf-8">
<title>KELVA Finance</title>
<link rel="stylesheet" href="https://fonts.googleapis.com/css2?family=Poppins:ital,wght@0,400;0,500;0,600;0,700;0,800;1,800&display=swap">
<style>
:root{
  --orange:#e8694a;
  --ink:#111111;
  --dark:#161616;
  --text:#2b2b2b;
  --muted:#8a8a8a;
  --field:#eeeeee;
  --white:#ffffff;
}
*{box-sizing:border-box;margin:0;padding:0}
html,body{width:1200px;height:3628px;overflow:hidden}
body{position:relative;font-family:'Poppins',sans-serif;color:var(--text);background:var(--white)}
.abs{position:absolute}
.btn{position:absolute;display:flex;align-items:center;justify-content:center;background:var(--orange);color:var(--white);font-size:14px;font-weight:500;text-transform:uppercase;text-decoration:none}
.photo{position:absolute}
.heading{font-weight:800;font-style:italic;color:var(--ink);text-align:center;text-transform:uppercase;letter-spacing:-0.5px}
.rule{display:flex;gap:4px;justify-content:center;margin-top:12px}
.rule span{display:block;width:18px;height:3px;background:var(--orange);transform:skewX(-30deg)}
.copy{font-size:15px;line-height:26px;text-align:center;color:var(--text)}

/* header & hero */
.hero{position:absolute;left:0;top:0;width:1200px;height:668px}
.brand{position:absolute;display:flex;align-items:center;gap:10px;color:var(--white);font-weight:700;font-size:30px;letter-spacing:0.5px}
.brand .divider{width:2px;height:38px;background:var(--white)}
.brand .sub{font-size:24px}
.nav{position:absolute;left:418px;top:34px;display:flex;gap:24px;font-size:14px;font-weight:500;color:var(--white)}
.nav a{color:inherit;text-decoration:none;text-transform:uppercase;position:relative;padding-bottom:8px}
.nav a.active::after{content:"";position:absolute;left:0;right:0;bottom:0;height:2px;background:var(--white)}
.call{left:960px;top:22px;width:185px;height:44px;font-size:15px;gap:8px;text-transform:none}
.hero-text{position:absolute;left:111px;top:218px;border-left:4px solid var(--orange);padding-left:18px;width:460px}
.hero-text h1{font-weight:800;font-size:42px;color:var(--white);line-height:1.1}
.hero-text h1 span{font-weight:400}
.hero-text p{color:var(--white);font-size:17.5px;line-height:26px;margin-top:14px}
.dots{position:absolute;left:111px;top:568px;display:flex;gap:8px;align-items:center}
.dots i{display:block;width:12px;height:12px;border-radius:50%;background:#8a8a8a}
.dots i.on{width:18px;height:18px;background:var(--white)}

/* feature rows */
.frame{position:absolute;background:var(--orange)}
.frame .photo{inset:0}
.feature{position:absolute;text-align:center}
.feature .heading{font-size:34px}

/* who we are */
.who{position:absolute;left:0;top:2088px;width:1200px;height:455px;background:var(--ink)}
.who-text{position:absolute;left:130px;top:2170px;width:450px;text-align:center;color:var(--white)}
.who-text h2{font-weight:800;font-style:italic;font-size:34px;text-transform:uppercase}
.who-text p{font-size:15px;line-height:25.7px;margin-top:8px}

/* calculator */
.calc-title{position:absolute;left:0;width:1258px;top:2650px;font-size:34px}
.field-label{position:absolute;left:218px;font-size:14.5px;color:#555}
.field{position:absolute;left:211px;width:395px;height:50px;background:var(--field);font-size:13px;color:#aaa;padding-left:16px;display:flex;align-items:center}
.ticks{position:absolute;left:211px;top:3088px;width:395px;display:flex;justify-content:space-between;font-size:11px;color:#555;padding:0 4px}
.panel{position:absolute;left:629px;top:2737px;width:361px;height:362px;background:linear-gradient(160deg,#1d2330 0%,#2a1d1d 45%,#7a2a1e 70%,#151515 100%);color:var(--white)}
.panel h3{position:absolute;left:22px;top:18px;font-size:24px;font-weight:700}
.panel .amt{position:absolute;left:22px;top:66px;font-size:25px;font-weight:700;color:var(--orange)}
.panel .amt small{font-size:14px;font-weight:400;color:var(--white);margin-left:6px}
.panel .go{position:absolute;left:27px;top:262px;font-size:14px;font-weight:700}
.panel .mail{position:absolute;left:23px;top:293px;width:304px;height:44px;border:2px solid var(--white);font-size:12px;padding-left:14px;display:flex;align-items:center;background:rgba(0,0,0,.55)}

/* footer */
.footer{position:absolute;left:0;top:3185px;width:1200px;height:443px;background:linear-gradient(180deg,#2a2a2a 0%,#1a1a1a 60%,#111 100%);color:var(--white)}
.col{position:absolute;top:166px;font-size:14.5px}
.col h4{font-weight:800;font-style:italic;font-size:15px;text-transform:uppercase;margin-bottom:12px}
.col li{list-style:none;line-height:25.7px;color:#d9d9d9}
.contact-row{display:flex;gap:16px;align-items:flex-start;line-height:25.7px;color:#d9d9d9}
.contact-row svg{flex:none;margin-top:6px}
.news-input{width:280px;height:40px;border:2px solid var(--white);font-size:13px;padding-left:18px;display:flex;align-items:center}
.news-btn{position:static;width:125px;height:40px;margin-top:14px;font-size:14px}
.copyright{position:absolute;left:0;width:1200px;top:380px;text-align:center;font-size:13px}
</style>
</head>
<body>

<section class="hero">
  <svg class="abs" style="left:0;top:0" width="1200" height="668" viewBox="0 0 1200 668">
    <defs>
      <linearGradient id="heroBg" x1="0" y1="0" x2="1" y2="1">
        <stop offset="0" stop-color="#1c1c1c"/><stop offset="1" stop-color="#0f0f0f"/>
      </linearGradient>
      <linearGradient id="heroPhoto" x1="0" y1="0" x2="1" y2="1">
        <stop offset="0" stop-color="#cfc6bd"/><stop offset="0.5" stop-color="#b9aea5"/><stop offset="1" stop-color="#8f8a88"/>
      </linearGradient>
    </defs>
    <rect width="1200" height="642" fill="url(#heroBg)"/>
    <polygon points="745,92 1200,92 1200,668 470,668 470,642 480,642" fill="#ffffff"/>
    <polygon points="760,96 1200,96 1200,668 498,668" fill="url(#heroPhoto)" role="img" aria-label="Smiling businesswoman holding up car keys and a folder"/>
  </svg>

  <div class="brand" style="left:111px;top:22px"><span>KELVA</span><span class="divider"></span><span class="sub">Finance</span></div>

  <nav class="nav">
    <a class="active" href="#">Home</a>
    <a href="#">Vehicle</a>
    <a href="#">Equipment</a>
    <a href="#">Who We Are</a>
    <a href="#">Contact Us</a>
  </nav>
  <a class="btn call" href="#">
    <svg width="12" height="12" viewBox="0 0 24 24"><path fill="#fff" d="M6.6 10.8a15.1 15.1 0 0 0 6.6 6.6l2.2-2.2a1 1 0 0 1 1-.25 11.4 11.4 0 0 0 3.6.57 1 1 0 0 1 1 1V20a1 1 0 0 1-1 1A17 17 0 0 1 3 4a1 1 0 0 1 1-1h3.5a1 1 0 0 1 1 1c0 1.25.2 2.45.57 3.6a1 1 0 0 1-.25 1z"/></svg>
    +1 555 014 2270
  </a>

  <div class="hero-text">
    <h1>KELVA <span>FINANCE</span></h1>
    <p>KELVA Finance has nearly 20 years industry experience, so we certainly understand personal and business lending.</p>
  </div>
  <a class="btn" href="#" style="left:111px;top:377px;width:137px;height:44px">Get Started</a>
  <div class="dots"><i class="on"></i><i></i><i></i><i></i></div>
</section>

<!-- why choose us -->
<div class="frame" style="left:111px;top:772px;width:490px;height:324px">
  <div class="photo" style="left:14px;right:14px;top:0;bottom:0;clip-path:polygon(0 0,100% 0,100% 100%,0 100%);background:linear-gradient(135deg,#6b5a4e,#a88f7c 50%,#3d3530)" role="img" aria-label="Happy couple sitting in a new car holding the keys"></div>
</div>
<div class="feature" style="left:628px;top:828px;width:430px">
  <h2 class="heading">Why Choose Us?</h2>
  <div class="rule"><span></span><span></span></div>
  <p class="copy" style="margin-top:14px">Well, because we're here to help you! We care about outcomes AND helping you achieve a stress and enjoyable lending experience.</p>
</div>
<a class="btn" href="#" style="left:776px;top:1002px;width:135px;height:44px">Learn More</a>

<!-- vehicle loan -->
<div class="frame" style="left:598px;top:1183px;width:490px;height:325px">
  <div class="photo" style="left:14px;right:14px;top:0;bottom:0;background:linear-gradient(135deg,#2b3a55,#8a98aa 50%,#3a3a44)" role="img" aria-label="Car dealer handing keys to smiling customers at a showroom desk"></div>
</div>
<div class="feature" style="left:140px;top:1240px;width:430px">
  <h2 class="heading">Vehicle Loan</h2>
  <div class="rule"><span></span><span></span></div>
  <p class="copy" style="margin-top:14px">While you focus on getting the right car, we will focus on getting you the right finance.</p>
</div>
<a class="btn" href="#" style="left:286px;top:1397px;width:135px;height:44px">Apply Now</a>

<!-- equipment -->
<div class="frame" style="left:111px;top:1594px;width:490px;height:364px">
  <div class="photo" style="left:14px;right:14px;top:0;bottom:0;background:linear-gradient(135deg,#c9ccd2,#7d8592 50%,#3b3f47)" role="img" aria-label="Business people reviewing documents and a tablet at a desk"></div>
</div>
<div class="feature" style="left:625px;top:1585px;width:450px">
  <h2 class="heading">Equipment</h2>
  <div class="rule"><span></span><span></span></div>
  <p class="copy" style="margin-top:14px">At KELVA, we help businesses of all sizes to secure funding in the form of a business loan for asset purchases from either a bank or private lender.</p>
  <p class="copy" style="margin-top:24px">Our dedicated Equipment Finance specialists have extensive industry experience across the agricultural, construction and earthmoving sectors. We'll work with you to understand the specific needs that face your business to keep your equipment up to date.</p>
</div>
<a class="btn" href="#" style="left:776px;top:1911px;width:135px;height:44px">Apply Now</a>

<!-- who we are -->
<section class="who">
  <div class="photo" style="left:600px;top:0;width:600px;height:455px;background:radial-gradient(ellipse at 45% 60%,#3a4f7a 0%,#15223c 50%,#0a0f1c 100%)" role="img" aria-label="Hand holding a tablet projecting glowing financial charts"></div>
</section>
<svg class="abs" style="left:107px;top:2040px" width="494" height="552" viewBox="0 0 494 552">
  <polygon points="247,0 494,130 494,422 247,552 0,422 0,130" fill="#ffffff"/>
  <polygon points="247,16 480,138 480,414 247,536 14,414 14,138" fill="#e8694a"/>
</svg>
<div class="who-text">
  <h2>Who We Are</h2>
  <p>The goal of KELVA Finance is to build on the track record of the KELVA business and to create a new benchmark in the Australia's Asset Finance industry, providing good old fashioned localised service that delivers the assets you want when you need them and structured to recognise asset useful life while being sensitive to cashflow.</p>
</div>
<a class="btn" href="#" style="left:287px;top:2422px;width:135px;height:44px;background:var(--white);color:var(--orange)">Learn More</a>

<!-- calculator -->
<h2 class="heading calc-title">Finance Repayment Calculator</h2>
<div class="field-label" style="top:2733px">Loan Amount*</div>
<div class="field" style="top:2763px">$ 1,40,000</div>
<div class="field-label" style="top:2836px">Deposit*</div>
<div class="field" style="top:2866px">$ 1,40,000</div>
<div class="field-label" style="top:2939px">Interest Rate*</div>
<div class="field" style="top:2969px">% 10.5</div>
<div class="field-label" style="top:3042px">Payment Term*</div>
<div class="field-label" style="top:3042px;left:545px">(years)</div>
<svg class="abs" style="left:211px;top:3064px" width="395" height="20" viewBox="0 0 395 20">
  <rect x="0" y="8" width="395" height="4" fill="#e6e6e6"/>
  <rect x="0" y="8" width="198" height="4" fill="#e8694a"/>
  <rect x="192" y="4" width="12" height="12" fill="#e8694a" stroke="#111" stroke-width="2" transform="rotate(45 198 10)"/>
</svg>
<div class="ticks"><span>1</span><span>2</span><span>3</span><span>4</span><span>5</span><span>6</span><span>7</span></div>

<div class="panel" role="img" aria-label="Red sports car in a dark studio behind the payment summary">
  <h3>MONTHLY PAYMENT</h3>
  <div class="amt">$ 25,500.000<small>Nemo enim ipsam</small></div>
  <div class="go">Get Started Now!!</div>
  <div class="mail">Enter your email</div>
</div>

<!-- footer -->
<footer class="footer">
  <div class="photo" style="inset:0;background:linear-gradient(180deg,rgba(60,60,60,.25),rgba(0,0,0,.5))" role="img" aria-label="Dim city skyline at dusk"></div>
  <div class="brand" style="left:489px;top:86px"><span>KELVA</span><span class="divider"></span><span class="sub">Finance</span></div>

  <div class="col" style="left:111px">
    <h4>Quick Links</h4>
    <ul><li>Home</li><li>Vehicle</li><li>Equipment</li><li>Who We Are</li><li>Contact Us</li></ul>
  </div>
  <div class="col" style="left:289px">
    <h4>Resources</h4>
    <ul><li>Lorem ipsum dolor</li><li>Sit amet, consectetur</li><li>Adipiscing elit, sed do</li><li>Eiusmod tempor</li><li>Incididunt ulabore</li></ul>
  </div>
  <div class="col" style="left:520px">
    <h4>Contact Us</h4>
    <div class="contact-row">
      <svg width="11" height="14" viewBox="0 0 12 16"><path fill="#ddd" d="M6 0a6 6 0 0 0-6 6c0 4.5 6 10 6 10s6-5.5 6-10a6 6 0 0 0-6-6zm0 8.5A2.5 2.5 0 1 1 6 3.5a2.5 2.5 0 0 1 0 5z"/></svg>
      <div>123,Lorem ipsum dolor<br>Sit amet, consec</div>
    </div>
    <div class="contact-row" style="margin-top:25px">
      <svg width="12" height="12" viewBox="0 0 24 24"><path fill="#ddd" d="M6.6 10.8a15.1 15.1 0 0 0 6.6 6.6l2.2-2.2a1 1 0 0 1 1-.25 11.4 11.4 0 0 0 3.6.57 1 1 0 0 1 1 1V20a1 1 0 0 1-1 1A17 17 0 0 1 3 4a1 1 0 0 1 1-1h3.5a1 1 0 0 1 1 1c0 1.25.2 2.45.57 3.6a1 1 0 0 1-.25 1z"/></svg>
      <div>+1 555 014 2270</div>
    </div>
    <div class="contact-row">
      <svg width="13" height="10" viewBox="0 0 16 12"><path fill="#ddd" d="M0 0h16v1.5L8 7 0 1.5zM0 3.5l8 5.5 8-5.5V12H0z"/></svg>
      <div>hello@kelvafinance.example</div>
    </div>
  </div>
  <div class="col" style="left:804px">
    <h4>Subscribe Our Newsletter</h4>
    <div class="news-input">Email address</div>
    <a class="btn news-btn" href="#">Subscribe</a>
  </div>

  <div class="copyright">© Copyrights 2022 Company name | All Rights Reserved</div>
</footer>

</body>
</html>
```